Flyer-Design für Aufbereiter von Fahrzeugen
Zielgruppe
Wir reinigen und aufbereiten (polieren, versiegeln) Fahrzeuge, vorwiegend Autos. Zusätzlich leihen wir Personal an Autowerkstätten für Servicereinigungen und Fahrzeugaufbereitung an. Unsere Kunden sind Privatpersonen: Junge Autofan aus der Tuningszene und gutsituierte mit Luxusautos. Weitere Kunden sind Gewerbliche für professionelle Fahrzeugaufbereitung und Manpower ausleihen.
Hier finden Sie unsere Tätigkeiten https://www.wagenglanz-beispiel.ch/unsere-leistungen/
Aufgabenstellung
Mit diesem Flyer wollen wir im besonderen die private Kundschaft ansprechen: Fahrzeugreinigung und -aufbereitung mit Hightech-Ergebnis. Der Flyer, A4, legen wir 1x zusammen und in ein durchsichtiges Couvert C5, sodass von beiden Seiten der Flyer gelesen werden kann. Wir verteilen ihn meistens nach einem Gespräch an Interessierte. Auf der Rückseite der Visitenkarte steht bei uns "Treten Sie glänzend auf..." und auf dem TShirt steht seitlich "we clean your dream" leuchtgrün/gelb. Die Internetseite ist mal so eine Erstausgabe, welche wir in einem späteren Zeitpunkt auch nochmals updaten wollen.
Bei Verwendung von Foto Nr. 123122 bitte Uhr entfernen

```html
<!DOCTYPE html>
<html lang="de">
<head>
<meta charset="utf-8">
<title>Wagenglanz Flyer</title>
<link rel="stylesheet" href="https://fonts.googleapis.com/css2?family=Bebas+Neue&family=Michroma&family=Nunito+Sans:wght@400;800&display=swap">
<style>
:root{
  --green:#74b935;
  --green-light:#9ac82e;
  --black:#1b1b1b;
  --white:#ffffff;
  --bg:#efefef;
}
*{margin:0;padding:0;box-sizing:border-box}
html,body{width:1200px;height:827px;overflow:hidden;background:var(--bg)}
.sheet{position:absolute;top:53px;width:500px;height:707px;overflow:hidden;
  background:radial-gradient(ellipse at 50% 55%,var(--green-light) 0%,var(--green) 70%)}
.front{left:72px}
.back{left:622px}
.stripe-wide{position:absolute;left:186px;width:128px;background:var(--black)}
.stripe-thin{position:absolute;width:6px;background:var(--black)}
.front .stripe-wide,.front .stripe-thin{top:0;bottom:0}
.headline{position:absolute;left:0;width:500px;text-align:center;font-family:"Bebas Neue",sans-serif;font-weight:400;
  color:var(--white);text-shadow:2px 3px 4px rgba(0,0,0,.35);white-space:nowrap;line-height:1}
.front .headline{top:100px;font-size:60px;letter-spacing:.5px}
.car-photo{position:absolute;left:39px;top:222px;width:443px;height:267px;border-radius:40px 40px 20px 20px;
  background:linear-gradient(180deg,#b7d94a 0%,#8cc43a 45%,#3a3f2a 70%,#2a2d22 100%);
  box-shadow:0 14px 18px rgba(0,0,0,.3)}
.site{position:absolute;left:24px;bottom:24px;font-family:"Michroma",sans-serif;font-size:10px;color:var(--white);
  text-shadow:1px 1px 2px rgba(0,0,0,.4)}
.brand-oval{position:absolute;left:343px;top:617px;width:133px;height:67px;border-radius:50%;background:var(--white);
  display:flex;align-items:center;justify-content:center;box-shadow:0 3px 6px rgba(0,0,0,.25)}
.brand-name{font-family:"Michroma",sans-serif;font-size:10px;color:var(--green)}
.back .stripe-frame{position:absolute;left:179px;top:0;width:142px;height:515px;background:var(--green)}
.back .stripe-wide{top:0;height:509px}
.back .stripe-thin{top:0;height:515px}
.back .headline{top:26px;font-size:50px}
.service{position:absolute;width:140px;height:140px;border-radius:50%;border:6px solid var(--black);
  box-shadow:0 6px 10px rgba(0,0,0,.35)}
.service.light{border-color:var(--white)}
.service-photo{position:absolute;inset:0;border-radius:50%}
.service-label{position:absolute;inset:0;display:flex;align-items:center;justify-content:center;text-align:center;
  font-family:"Michroma",sans-serif;font-size:8px;line-height:1.2;color:var(--white);text-shadow:1px 1px 2px rgba(0,0,0,.7);padding:0 6px}
.price{position:absolute;width:40px;height:40px;border-radius:50%;background:rgba(235,235,235,.85);
  display:flex;align-items:center;justify-content:center;font-family:"Nunito Sans",sans-serif;font-weight:800;font-size:12px;color:#333}
.price small{font-size:8px}
.price.accent{background:rgba(116,185,53,.9);color:#2a2a2a}
.band{position:absolute;left:0;width:500px;top:515px;height:41px;background:var(--black)}
.band-inner{position:absolute;left:0;right:0;top:8px;height:25px;border-top:2px solid var(--green);border-bottom:2px solid var(--green);
  display:flex;align-items:center;justify-content:center;font-family:"Michroma",sans-serif;font-size:12px;color:var(--white)}
.reasons{position:absolute;left:92px;width:316px;top:563px;list-style:none;font-family:"Nunito Sans",sans-serif;
  font-size:7.3px;color:var(--white);text-align:center}
.reasons li{padding:3px 0 4px;border-bottom:1px solid var(--white);line-height:1.15}
.cta{position:absolute;left:40px;width:420px;top:656px;text-align:center;font-family:"Michroma",sans-serif;
  font-size:7.5px;color:var(--white)}
.footer{position:absolute;left:0;bottom:0;width:500px;height:24px;background:var(--black);display:flex;align-items:center;
  justify-content:center;font-family:"Nunito Sans",sans-serif;font-size:7.3px;color:var(--white)}
</style>
</head>
<body>
<section class="sheet front">
  <div class="stripe-thin" style="left:173px"></div>
  <div class="stripe-wide"></div>
  <div class="stripe-thin" style="left:321px"></div>
  <h1 class="headline">WE CLEAN YOUR DREAM</h1>
  <div class="car-photo" role="img" aria-label="Foto: leuchtgrüner Sportwagen mit schwarzen Rennstreifen, Frontansicht"></div>
  <p class="site">www.wagenglanz-beispiel.ch</p>
  <div class="brand-oval"><span class="brand-name">wagenglanz.ch</span></div>
</section>

<section class="sheet back">
  <div class="stripe-thin" style="left:173px"></div>
  <div class="stripe-frame"></div>
  <div class="stripe-wide"></div>
  <div class="stripe-thin" style="left:320px"></div>
  <h2 class="headline">TRETEN SIE GLÄNZEND AUF...</h2>

  <div class="service" style="left:23px;top:124px">
    <div class="service-photo" role="img" aria-label="Foto: Handwäsche eines Autos" style="background:radial-gradient(circle at 40% 40%,#8a5a3a,#3a2a22)"></div>
    <div class="service-label">Wäsche</div>
  </div>
  <div class="price" style="left:28px;top:225px">15<small>CHF</small></div>

  <div class="service light" style="left:179px;top:124px">
    <div class="service-photo" role="img" aria-label="Foto: gereinigter Fahrzeuginnenraum" style="background:linear-gradient(160deg,#e8e8e8,#9a9a9a 60%,#8cc43a)"></div>
    <div class="service-label">Innenreinigung</div>
  </div>
  <div class="price accent" style="left:193px;top:225px">12<small>CHF</small></div>

  <div class="service" style="left:335px;top:124px">
    <div class="service-photo" role="img" aria-label="Foto: Polieren der Karosserie" style="background:radial-gradient(circle at 55% 45%,#9a9a9a,#2a2a2a)"></div>
    <div class="service-label">Aussen - Behandlung<br>&amp; Aufbereitung</div>
  </div>
  <div class="price" style="left:435px;top:225px">25<small>CHF</small></div>

  <div class="service" style="left:23px;top:303px">
    <div class="service-photo" role="img" aria-label="Foto: versiegelter Sportwagen mit Wasserperlen" style="background:radial-gradient(circle at 50% 50%,#6a4a3a,#2a2222)"></div>
    <div class="service-label">Versiegelung<br>mit Glanz-<br>&amp; Schutzwirkung</div>
  </div>
  <div class="price" style="left:28px;top:403px">18<small>CHF</small></div>

  <div class="service light" style="left:179px;top:303px">
    <div class="service-photo" role="img" aria-label="Foto: foliertes Sportcoupé" style="background:linear-gradient(180deg,#b8c8a0,#3a2f4a 55%,#8cc43a)"></div>
    <div class="service-label">Folieren &amp; Tönen</div>
  </div>
  <div class="price accent" style="left:255px;top:403px">120<small>CHF</small></div>

  <div class="service" style="left:335px;top:303px">
    <div class="service-photo" role="img" aria-label="Foto: Fahrzeugkontrolle auf der Hebebühne" style="background:linear-gradient(180deg,#6a6a6a,#8cc43a)"></div>
    <div class="service-label">Kontrolle - Qualität</div>
  </div>
  <div class="price" style="left:435px;top:403px">59<small>CHF</small></div>

  <div class="band"><div class="band-inner">Warum mit uns?</div></div>

  <ul class="reasons">
    <li>Wir arbeiten professionell, setzen auf High-End-Qualität</li>
    <li>Mit uns gewinnen Sie Zeit. Anruf genügt, alles Übrige erledigen wir</li>
    <li>Mit uns sparen Sie Geld. Weniger Fixkosten, variable nur bei Bedarf</li>
    <li>Entlasten Sie sich. Wir übernehmen Verantwortung für unsere Arbeit. Ihr Zusatznutzen:<br>Wir desinfizieren &amp; geruchsneutralisieren</li>
    <li>Fahrzeuginnenraum und Klimaanlage</li>
  </ul>
  <p class="cta">Profitieren Sie von unserem Können. Sprechen Sie uns an!</p>

  <footer class="footer">H 076 000 12 34 | F 041 000 56 78 | info@wagenglanz-beispiel.ch | www.wagenglanz-beispiel.ch</footer>
</section>
</body>
</html>
```